Baby Care Print Log for Nannies and Parents- Creating a brand/style I can use across different forms

I am creating a notebook for babysitters to use to communicate with parents about the children they care for. I will be creating many different forms (emergency contacts, daily logs, shopping lists, etc.)
I need a look and feel from which to style these forms from. I am starting by designing the daily baby care log. I need a designer to take my Word doc with just text on it, and create a visual approach to make this visually appealing.
I do not want this to be extremely "babyish" with cartoon styling. I want it to be more of a professional looking style. I would like to be able to color each different document a different color palette, yet keep the similar look and feel. My logo is attached for inspiration. I use real photography across my website quillharborpages.com.
Updates
I will be re-designing my Wordpress website based on what design I like best and also will need other forms completed once I pick a design. I am hoping to work with someone who I can hire for further development needs as well. Added Saturday, February 11, 2017
Target Market(s)
Professional Parents
Industry/Entity Type
Education
Requirements
Must have
- color, pop, visual appeal
- Please use the color in my logo and any complementary colors that you think work well with it. I definitely like colored patterns, ombre, colored backgrounds, etc. I'd prefer for it not to be completely white with only pops of color here and there.
Nice to have
- My logo somewhere subtly on the form
- Photography elements
Should not have
- cartoon images of babies, etc. I use real photography across my website with the exception of my logo umbrella.

```html
<!DOCTYPE html>
<html lang="en">
<head>
<meta charset="utf-8">
<title>Quill Harbor Pages – Daily Baby Care Log</title>
<link href="https://fonts.googleapis.com/css2?family=Mulish:wght@400;600;700&display=swap" rel="stylesheet">
<style>
  :root{
    --backdrop:#bdbdbd;
    --paper:#ffffff;
    --ink:#3d3d3d;
    --blue-band:#40c4e2;
    --blue-deep:#22a9ba;
    --blue-accent:#1fa3bd;
    --blue-row-a:#bfe5ee;
    --blue-row-b:#e7f6fb;
    --pink-band:#f294bd;
    --pink-deep:#ec4f95;
    --pink-accent:#e6307f;
    --pink-row-a:#f9c9dd;
    --pink-row-b:#fde6ef;
  }
  *{box-sizing:border-box;margin:0;padding:0}
  html,body{width:1200px;height:898px;overflow:hidden;background:var(--backdrop)}
  body{position:relative;font-family:'Mulish',sans-serif;color:var(--ink)}

  .log-sheet{position:absolute;top:118px;width:493px;height:638px;background:var(--paper);overflow:hidden}
  .log-sheet--blue{left:71px;--band:var(--blue-band);--deep:var(--blue-deep);--accent:var(--blue-accent);--row-a:var(--blue-row-a);--row-b:var(--blue-row-b)}
  .log-sheet--pink{left:643px;top:118px;height:640px;--band:var(--pink-band);--deep:var(--pink-deep);--accent:var(--pink-accent);--row-a:var(--pink-row-a);--row-b:var(--pink-row-b)}

  .sheet-header,.sheet-footer{position:absolute;left:0;width:493px}
  .sheet-header{top:0;height:70px}
  .sheet-footer{bottom:0;height:56px}
  .band{fill:var(--band)}
  .swoosh{fill:var(--deep)}

  .brand{position:absolute;top:44px;left:0;width:493px;display:flex;justify-content:center;align-items:center;gap:8px}
  .brand-mark{width:16px;height:16px;border-radius:50%;background:var(--band)}
  .brand-name{font-size:21px;font-weight:700;color:var(--ink);letter-spacing:.2px}

  .label{position:absolute;font-size:11px;font-weight:600;color:var(--accent);white-space:nowrap}
  .rule{position:absolute;height:0;border-bottom:1px dotted var(--accent)}

  .grid{position:absolute;border:1px solid var(--band);border-collapse:collapse;font-size:8px;table-layout:fixed}
  .grid th.grid-title{background:var(--deep);color:#fff;font-size:11px;font-weight:600;height:17px;border:none}
  .grid th.col{background:var(--row-b);font-weight:400;color:var(--ink);height:17px;text-align:left;padding-left:6px;border-right:1px solid #fff}
  .grid td{height:15px;border-right:1px solid #fff;border-top:1px solid #fff}
  .grid tr:nth-child(odd) td{background:var(--row-a)}
  .grid tr:nth-child(even) td{background:var(--row-b)}
  .grid--nap{left:52px;top:151px;width:166px}
  .grid--feed{left:231px;top:151px;width:210px}

  .diaper-head{position:absolute;top:309px;font-size:8.5px}
  .diaper-time{position:absolute;left:52px;width:22px;border-bottom:1px dotted var(--accent)}
  .box{position:absolute;width:13px;height:13px;border:1px solid var(--accent)}

  .mood{position:absolute;display:flex;align-items:center;gap:5px;font-size:8.5px}
  .mood-dot{width:20px;height:20px;border-radius:50%;border:1.5px solid var(--accent);display:inline-block}

  .supply{position:absolute;display:flex;align-items:center;gap:9px;font-size:9.5px}
  .supply-ring{width:14px;height:14px;border-radius:50%;border:1px solid var(--accent);display:inline-block}

  .photo{position:absolute;left:367px;top:506px;width:126px;height:112px;border-radius:48% 48% 0 0;
    background:radial-gradient(ellipse at 55% 40%,#f6d2bf 0%,#eab59b 55%,rgba(255,255,255,0) 72%)}
</style>
</head>
<body>

<!-- Blue edition -->
<article class="log-sheet log-sheet--blue">
  <svg class="sheet-header" viewBox="0 0 493 70" aria-hidden="true">
    <path class="band" d="M0 0H493V30Q250 8 0 32Z"/>
    <path class="swoosh" d="M290 18Q420 22 493 40V66Q420 32 290 18Z"/>
  </svg>
  <div class="brand"><span class="brand-mark"></span><span class="brand-name">Quill Harbor Pages</span></div>

  <span class="label" style="left:52px;top:83px">Name:</span><div class="rule" style="left:93px;top:94px;width:194px"></div>
  <span class="label" style="left:302px;top:83px">Date:</span><div class="rule" style="left:333px;top:94px;width:108px"></div>
  <span class="label" style="left:52px;top:107px">Parent Notes:</span><div class="rule" style="left:128px;top:118px;width:313px"></div>
  <div class="rule" style="left:52px;top:134px;width:389px"></div>

  <table class="grid grid--nap">
    <tr><th class="grid-title" colspan="2">Nap Time</th></tr>
    <tr><th class="col" style="width:50px">Time</th><th class="col">How Long</th></tr>
    <tr><td></td><td></td></tr><tr><td></td><td></td></tr><tr><td></td><td></td></tr>
    <tr><td></td><td></td></tr><tr><td></td><td></td></tr><tr><td></td><td></td></tr>
  </table>
  <table class="grid grid--feed">
    <tr><th class="grid-title" colspan="5">Feeding</th></tr>
    <tr><th class="col" style="width:35px">Time</th><th class="col" style="width:50px;padding-left:3px">Milk(Type)</th><th class="col" style="width:43px">Water</th><th class="col" style="width:43px">Food</th><th class="col" style="padding-left:3px">Amount</th></tr>
    <tr><td></td><td></td><td></td><td></td><td></td></tr><tr><td></td><td></td><td></td><td></td><td></td></tr>
    <tr><td></td><td></td><td></td><td></td><td></td></tr><tr><td></td><td></td><td></td><td></td><td></td></tr>
    <tr><td></td><td></td><td></td><td></td><td></td></tr><tr><td></td><td></td><td></td><td></td><td></td></tr>
  </table>

  <span class="label" style="left:52px;top:288px">Diapers</span>
  <span class="diaper-head" style="left:52px">Time</span>
  <span class="diaper-head" style="left:93px">Wet</span>
  <span class="diaper-head" style="left:125px">BM</span>
  <div class="diaper-time" style="top:339px"></div><span class="box" style="left:93px;top:327px"></span><span class="box" style="left:125px;top:327px"></span>
  <div class="diaper-time" style="top:363px"></div><span class="box" style="left:93px;top:351px"></span><span class="box" style="left:125px;top:351px"></span>
  <div class="diaper-time" style="top:387px"></div><span class="box" style="left:93px;top:375px"></span><span class="box" style="left:125px;top:375px"></span>
  <div class="diaper-time" style="top:411px"></div><span class="box" style="left:93px;top:399px"></span><span class="box" style="left:125px;top:399px"></span>
  <div class="diaper-time" style="top:435px"></div><span class="box" style="left:93px;top:423px"></span><span class="box" style="left:125px;top:423px"></span>
  <div class="diaper-time" style="top:459px"></div><span class="box" style="left:93px;top:447px"></span><span class="box" style="left:125px;top:447px"></span>
  <div class="diaper-time" style="top:483px"></div><span class="box" style="left:93px;top:471px"></span><span class="box" style="left:125px;top:471px"></span>
  <div class="diaper-time" style="top:507px"></div><span class="box" style="left:93px;top:495px"></span><span class="box" style="left:125px;top:495px"></span>

  <span class="label" style="left:174px;top:288px">Mood</span>
  <span class="mood" style="left:174px;top:309px"><i class="mood-dot"></i>Happy</span>
  <span class="mood" style="left:247px;top:309px"><i class="mood-dot"></i>Unsettled</span>
  <span class="mood" style="left:323px;top:309px"><i class="mood-dot"></i>Tired</span>
  <span class="mood" style="left:384px;top:309px"><i class="mood-dot"></i>Chatty</span>
  <span class="mood" style="left:174px;top:339px"><i class="mood-dot"></i>Energetic</span>
  <span class="mood" style="left:249px;top:339px"><i class="mood-dot"></i>Sad</span>
  <span class="mood" style="left:324px;top:339px"><i class="mood-dot"></i>Quiet</span>

  <span class="label" style="left:174px;top:372px">Today’s Activities</span><div class="rule" style="left:267px;top:383px;width:174px"></div>
  <div class="rule" style="left:174px;top:399px;width:267px"></div>
  <div class="rule" style="left:174px;top:416px;width:267px"></div>

  <span class="label" style="left:174px;top:432px">Supplies Needed Soon</span>
  <span class="supply" style="left:171px;top:453px"><i class="supply-ring"></i>Diapers</span>
  <span class="supply" style="left:271px;top:453px"><i class="supply-ring"></i>Milk/Formula</span>
  <span class="supply" style="left:366px;top:453px"><i class="supply-ring"></i>Wet Wipes</span>
  <span class="supply" style="left:171px;top:475px"><i class="supply-ring"></i>Diaper Cream</span>
  <span class="supply" style="left:271px;top:475px"><i class="supply-ring"></i>Cereal</span>
  <span class="supply" style="left:366px;top:475px"><i class="supply-ring"></i>Baby Food</span>
  <span class="supply" style="left:171px;top:495px"><i class="supply-ring"></i>Other:</span>

  <span class="label" style="left:52px;top:526px">Special Notes</span><div class="rule" style="left:127px;top:537px;width:266px"></div>
  <div class="rule" style="left:52px;top:551px;width:341px"></div>
  <div class="rule" style="left:52px;top:568px;width:341px"></div>
  <div class="rule" style="left:52px;top:585px;width:341px"></div>

  <svg class="sheet-footer" viewBox="0 0 493 56" aria-hidden="true">
    <path class="swoosh" d="M0 0Q70 30 280 42Q90 40 0 24Z"/>
    <path class="band" d="M0 30Q180 50 493 36V56H0Z"/>
  </svg>
  <div class="photo" role="img" aria-label="Photograph of a smiling baby lying on its tummy"></div>
</article>

<!-- Pink edition -->
<article class="log-sheet log-sheet--pink">
  <svg class="sheet-header" viewBox="0 0 493 70" aria-hidden="true">
    <path class="band" d="M0 0H493V30Q250 8 0 32Z"/>
    <path class="swoosh" d="M290 18Q420 22 493 40V66Q420 32 290 18Z"/>
  </svg>
  <div class="brand" style="top:50px"><span class="brand-mark"></span><span class="brand-name">Quill Harbor Pages</span></div>

  <span class="label" style="left:52px;top:83px">Name:</span><div class="rule" style="left:93px;top:94px;width:194px"></div>
  <span class="label" style="left:302px;top:83px">Date:</span><div class="rule" style="left:333px;top:94px;width:108px"></div>
  <span class="label" style="left:52px;top:107px">Parent Notes:</span><div class="rule" style="left:128px;top:118px;width:313px"></div>
  <div class="rule" style="left:52px;top:134px;width:389px"></div>

  <table class="grid grid--nap">
    <tr><th class="grid-title" colspan="2">Nap Time</th></tr>
    <tr><th class="col" style="width:50px">Time</th><th class="col">How Long</th></tr>
    <tr><td></td><td></td></tr><tr><td></td><td></td></tr><tr><td></td><td></td></tr>
    <tr><td></td><td></td></tr><tr><td></td><td></td></tr><tr><td></td><td></td></tr>
  </table>
  <table class="grid grid--feed">
    <tr><th class="grid-title" colspan="5">Feeding</th></tr>
    <tr><th class="col" style="width:35px">Time</th><th class="col" style="width:50px;padding-left:3px">Milk(Type)</th><th class="col" style="width:43px">Water</th><th class="col" style="width:43px">Food</th><th class="col" style="padding-left:3px">Amount</th></tr>
    <tr><td></td><td></td><td></td><td></td><td></td></tr><tr><td></td><td></td><td></td><td></td><td></td></tr>
    <tr><td></td><td></td><td></td><td></td><td></td></tr><tr><td></td><td></td><td></td><td></td><td></td></tr>
    <tr><td></td><td></td><td></td><td></td><td></td></tr><tr><td></td><td></td><td></td><td></td><td></td></tr>
  </table>

  <span class="label" style="left:52px;top:288px">Diapers</span>
  <span class="diaper-head" style="left:52px">Time</span>
  <span class="diaper-head" style="left:93px">Wet</span>
  <span class="diaper-head" style="left:125px">BM</span>
  <div class="diaper-time" style="top:339px"></div><span class="box" style="left:93px;top:327px"></span><span class="box" style="left:125px;top:327px"></span>
  <div class="diaper-time" style="top:363px"></div><span class="box" style="left:93px;top:351px"></span><span class="box" style="left:125px;top:351px"></span>
  <div class="diaper-time" style="top:387px"></div><span class="box" style="left:93px;top:375px"></span><span class="box" style="left:125px;top:375px"></span>
  <div class="diaper-time" style="top:411px"></div><span class="box" style="left:93px;top:399px"></span><span class="box" style="left:125px;top:399px"></span>
  <div class="diaper-time" style="top:435px"></div><span class="box" style="left:93px;top:423px"></span><span class="box" style="left:125px;top:423px"></span>
  <div class="diaper-time" style="top:459px"></div><span class="box" style="left:93px;top:447px"></span><span class="box" style="left:125px;top:447px"></span>
  <div class="diaper-time" style="top:483px"></div><span class="box" style="left:93px;top:471px"></span><span class="box" style="left:125px;top:471px"></span>
  <div class="diaper-time" style="top:507px"></div><span class="box" style="left:93px;top:495px"></span><span class="box" style="left:125px;top:495px"></span>

  <span class="label" style="left:174px;top:288px">Mood</span>
  <span class="mood" style="left:174px;top:309px"><i class="mood-dot"></i>Happy</span>
  <span class="mood" style="left:249px;top:309px"><i class="mood-dot"></i>Unsettled</span>
  <span class="mood" style="left:325px;top:309px"><i class="mood-dot"></i>Tired</span>
  <span class="mood" style="left:386px;top:309px"><i class="mood-dot"></i>Chatty</span>
  <span class="mood" style="left:174px;top:339px"><i class="mood-dot"></i>Energetic</span>
  <span class="mood" style="left:249px;top:339px"><i class="mood-dot"></i>Sad</span>
  <span class="mood" style="left:325px;top:339px"><i class="mood-dot"></i>Quiet</span>

  <span class="label" style="left:174px;top:372px">Today’s Activities</span><div class="rule" style="left:267px;top:383px;width:174px"></div>
  <div class="rule" style="left:174px;top:399px;width:267px"></div>
  <div class="rule" style="left:174px;top:416px;width:267px"></div>

  <span class="label" style="left:174px;top:432px">Supplies Needed Soon</span>
  <span class="supply" style="left:171px;top:453px"><i class="supply-ring"></i>Diapers</span>
  <span class="supply" style="left:271px;top:453px"><i class="supply-ring"></i>Milk/Formula</span>
  <span class="supply" style="left:366px;top:453px"><i class="supply-ring"></i>Wet Wipes</span>
  <span class="supply" style="left:171px;top:475px"><i class="supply-ring"></i>Diaper Cream</span>
  <span class="supply" style="left:271px;top:475px"><i class="supply-ring"></i>Cereal</span>
  <span class="supply" style="left:366px;top:475px"><i class="supply-ring"></i>Baby Food</span>
  <span class="supply" style="left:171px;top:495px"><i class="supply-ring"></i>Other:</span>

  <span class="label" style="left:52px;top:526px">Special Notes</span><div class="rule" style="left:127px;top:537px;width:266px"></div>
  <div class="rule" style="left:52px;top:551px;width:341px"></div>
  <div class="rule" style="left:52px;top:568px;width:341px"></div>
  <div class="rule" style="left:52px;top:585px;width:341px"></div>

  <svg class="sheet-footer" viewBox="0 0 493 56" aria-hidden="true">
    <path class="swoosh" d="M0 0Q70 30 280 42Q90 40 0 24Z"/>
    <path class="band" d="M0 30Q180 50 493 36V56H0Z"/>
  </svg>
  <div class="photo" style="top:508px" role="img" aria-label="Photograph of a smiling baby lying on its tummy"></div>
</article>

</body>
</html>
```